Commercial Construction Company

We need a business card design based on our current logo. We are a commercial general contractor based in Southern California that specializes in bank remodels. We would like to see designs that incorporate dark blue. The final design should portray an image of professionalism and quality.

If possible, I would like to add metallic foil to the design. Thank you

```html
<!DOCTYPE html>
<html lang="en">
<head>
<meta charset="utf-8">
<title>Harlow Civic Builders – Business Card</title>
<link href="https://fonts.googleapis.com/css2?family=Poppins:wght@300;400;600&display=swap" rel="stylesheet">
<style>
  :root {
    --brand-blue: #124a7e;
    --icon-blue: #1663ad;
    --ink: #151515;
    --paper: #ffffff;
    --page: #ffffff;
    --shadow: rgba(0, 0, 0, 0.28);
  }
  html, body {
    margin: 0;
    width: 1200px;
    height: 1200px;
    overflow: hidden;
    background: var(--page);
    font-family: "Poppins", sans-serif;
  }
  .card {
    position: absolute;
    left: 250px;
    width: 700px;
    height: 400px;
    box-shadow: 6px 8px 10px var(--shadow);
  }
  .card--front { top: 147px; background: var(--paper); }
  .card--back  { top: 653px; background: var(--brand-blue); }

  .brand {
    position: absolute;
    display: flex;
    align-items: center;
    gap: 14px;
  }
  .brand__dot {
    width: 54px;
    height: 54px;
    border-radius: 50%;
    flex: none;
  }
  .brand__name {
    font-weight: 600;
    font-size: 22px;
    line-height: 1.15;
  }
  .card--front .brand { left: 78px; top: 166px; }
  .card--front .brand__dot { background: var(--brand-blue); }
  .card--front .brand__name { color: var(--brand-blue); }

  .card--back .brand { left: 50%; top: 166px; transform: translateX(-50%); }
  .card--back .brand__dot { background: var(--paper); }
  .card--back .brand__name { color: var(--paper); font-size: 26px; }

  .divider {
    position: absolute;
    left: 328px;
    top: 118px;
    width: 1.5px;
    height: 165px;
    background: var(--ink);
  }

  .identity {
    position: absolute;
    right: 79px;
    top: 60px;
    text-align: right;
  }
  .identity__name {
    margin: 0;
    font-size: 33px;
    line-height: 1;
    color: var(--brand-blue);
    font-weight: 300;
  }
  .identity__name strong { font-weight: 600; }
  .identity__role {
    margin: 2px 0 0;
    font-size: 17px;
    color: var(--ink);
    font-weight: 400;
  }

  .contacts {
    position: absolute;
    right: 40px;
    top: 201px;
    margin: 0;
    padding: 0;
    list-style: none;
  }
  .contact {
    display: flex;
    align-items: center;
    justify-content: flex-end;
    gap: 11px;
    margin-bottom: 14px;
  }
  .contact__text {
    text-align: right;
    font-size: 16.5px;
    line-height: 17px;
    color: var(--ink);
  }
  .contact__icon { width: 28px; height: 28px; flex: none; }

  .back-web {
    position: absolute;
    left: 0;
    right: 0;
    top: 340px;
    text-align: center;
    color: var(--paper);
    font-size: 17px;
    letter-spacing: 3px;
    font-weight: 400;
  }
</style>
</head>
<body>

<section class="card card--front">
  <div class="brand">
    <span class="brand__dot"></span>
    <span class="brand__name">Harlow Civic<br>Builders</span>
  </div>

  <div class="divider"></div>

  <div class="identity">
    <h1 class="identity__name"><strong>Your</strong> Name</h1>
    <p class="identity__role">Designation here</p>
  </div>

  <ul class="contacts">
    <li class="contact">
      <span class="contact__text">+00 01234-56789<br>+00 01234-56789</span>
      <svg class="contact__icon" viewBox="0 0 28 28" aria-hidden="true">
        <circle cx="14" cy="14" r="14" fill="var(--icon-blue)"/>
        <path d="M10.2 7.5l2 3.2-1.3 1.6c.8 1.8 2.2 3.2 4 4l1.6-1.3 3.2 2-.9 2.4c-5.3-.2-9.8-4.7-10-10z" fill="#fff"/>
      </svg>
    </li>
    <li class="contact">
      <span class="contact__text">youremail@mailhost.com<br>www.yourweb.com</span>
      <svg class="contact__icon" viewBox="0 0 28 28" aria-hidden="true">
        <circle cx="14" cy="14" r="14" fill="var(--icon-blue)"/>
        <rect x="7" y="9" width="14" height="10" rx="1" fill="none" stroke="#fff" stroke-width="1.6"/>
        <path d="M7.5 9.5l6.5 5 6.5-5M7.5 18.5l4.5-4M20.5 18.5l-4.5-4" fill="none" stroke="#fff" stroke-width="1.4"/>
      </svg>
    </li>
    <li class="contact">
      <span class="contact__text">Your City Address<br>Street Location, California</span>
      <svg class="contact__icon" viewBox="0 0 28 28" aria-hidden="true">
        <circle cx="14" cy="14" r="14" fill="var(--icon-blue)"/>
        <path d="M14 6.5a5.5 5.5 0 0 0-5.5 5.5c0 4 5.5 9.5 5.5 9.5s5.5-5.5 5.5-9.5A5.5 5.5 0 0 0 14 6.5z" fill="#fff"/>
        <circle cx="14" cy="12" r="2" fill="var(--icon-blue)"/>
      </svg>
    </li>
  </ul>
</section>

<section class="card card--back">
  <div class="brand">
    <span class="brand__dot"></span>
    <span class="brand__name">Harlow Civic<br>Builders</span>
  </div>
  <p class="back-web">www.yourweb.com</p>
</section>

</body>
</html>
```